I would like alternative creative proposals for our website header at mirrowenhaven.com.au
The current is seen as a bit too drab and dark. We would like to liven it up a bit. The logo will remain although we are open to alternative representation or styling. All submitted designs should include a version that has the existing logo (we do use it within a black circle in other marketing).
The fundamental features of the header must be present including brand logo, search, cart etc.
We want to expand our concept of how the header could appear and function and how it represents our business. Other web site expects will be redesigned to align.
Please become familiar with our business and what we are trying to achieve before submitting a design. We are about health, organic products, chemical free low toxin living, environmental sustainability, all delivered in a modern socially friendly way accessible to all demographics and walks of life with our primary focus on Australia. Our primary target demographic is Australian women between 35 and 55. If you would like more info then please send us some questions.
Development and full design is outside the scoop of this proposal. We are looking for "mockup" proposals for the new website header initially.

```html
<!DOCTYPE html>
<html lang="en">
<head>
<meta charset="utf-8">
<title>Mirrowen Haven – Natural, Organic &amp; Toxin-Free Living</title>
<link href="https://fonts.googleapis.com/css2?family=Montserrat:wght@400;600;700&family=Open+Sans:wght@400;600&display=swap" rel="stylesheet">
<style>
:root{
  --purple:#6a4fb8;
  --purple-dark:#4b3a86;
  --pink:#e0457b;
  --ink:#333344;
  --muted:#8a8a99;
  --line:#e6e4ee;
  --soft:#f4f5fa;
  --footer:#3d3850;
  --footer-deep:#332f44;
  --white:#ffffff;
}
*{box-sizing:border-box;margin:0;padding:0}
html,body{width:1200px;height:2472px;overflow:hidden;background:var(--white)}
body{font-family:"Open Sans",Arial,sans-serif;color:var(--ink);font-size:13px;position:relative}
.abs{position:absolute}
h2,h3,.heading{font-family:"Montserrat",Arial,sans-serif}

/* header */
.topbar{top:0;left:0;width:1200px;height:22px;border-bottom:1px solid var(--line);font-size:11px;color:var(--muted)}
.topbar .phone{left:40px;top:4px}
.topbar .util{right:40px;top:4px;display:flex;gap:18px}
.brand{left:40px;top:30px;display:flex;align-items:center;gap:10px}
.brand .dot{width:38px;height:38px;border-radius:50%;background:var(--pink)}
.brand span{font-family:"Montserrat",Arial,sans-serif;font-weight:700;font-size:18px;color:var(--purple)}
.search{left:330px;top:36px;width:420px;height:30px;border:1px solid var(--line);border-radius:3px;display:flex;align-items:center;padding:0 10px;color:var(--muted);font-size:12px;justify-content:space-between}
.icons{right:40px;top:38px;display:flex;gap:22px}
.nav{top:90px;left:0;width:1200px;height:46px;border-top:1px solid var(--line);display:flex;justify-content:center;gap:30px;align-items:center;font-family:"Montserrat",Arial,sans-serif;font-size:12px;font-weight:600;color:var(--ink)}

/* hero */
.hero{top:136px;left:0;width:1200px;height:456px;background:linear-gradient(100deg,#1e2b2a 0%,#2f3d3a 45%,#6d4f4a 70%,#3a3230 100%)}
.hero .copy{width:1200px;top:150px;text-align:center;color:var(--white)}
.hero h1{font-family:"Montserrat",Arial,sans-serif;font-size:44px;font-weight:700;letter-spacing:1px}
.hero p{font-size:13px;margin-top:8px;opacity:.9}
.btn{display:inline-block;background:var(--purple);color:var(--white);font-family:"Montserrat",Arial,sans-serif;font-size:11px;font-weight:700;padding:10px 24px;border-radius:3px;text-transform:uppercase}
.hero .btn{margin-top:20px}
.arrow{width:26px;height:26px;background:rgba(255,255,255,.85);border-radius:2px;display:flex;align-items:center;justify-content:center}
.dots{top:420px;left:578px;display:flex;gap:8px}
.dots i{width:8px;height:8px;border-radius:50%;background:rgba(255,255,255,.5)}
.dots i:first-child{background:var(--white)}

/* section titles */
.section-title{width:1200px;left:0;text-align:center;color:var(--purple);font-size:22px;font-weight:700;letter-spacing:1px}
.section-title::after{content:"";display:block;width:40px;height:2px;background:var(--pink);margin:10px auto 0}

/* products */
.card{top:760px;width:160px}
.card .shot{height:230px;border:1px solid var(--line);display:flex;align-items:center;justify-content:center}
.card .shot div{width:90px;height:140px;border-radius:4px}
.card h4{font-size:12px;font-weight:600;margin-top:14px}
.card .sub{font-size:11px;color:var(--muted);margin-top:3px}
.card .price{font-size:12px;color:var(--pink);font-weight:600;margin-top:6px}

/* welcome */
.welcome{top:1072px;left:0;width:1200px;height:460px;background:var(--soft)}
.welcome .text{left:232px;top:100px;width:320px}
.welcome small{font-size:12px;color:var(--muted)}
.welcome h2{font-size:22px;line-height:1.25;color:var(--purple);margin-top:8px}
.welcome p{font-size:12px;color:var(--muted);line-height:1.6;margin-top:14px}
.ghost{display:inline-block;border:1px solid var(--purple);color:var(--purple);font-size:11px;padding:8px 20px;border-radius:3px;margin:22px 10px 0 0}
.tile{border-radius:2px}

/* brands */
.brands{top:1712px;left:192px;width:816px;display:flex;justify-content:space-between;align-items:center}
.brands span{font-family:"Montserrat",Arial,sans-serif;font-size:20px;font-weight:700;color:#3a3a44}

/* delivery */
.delivery{top:1820px;left:232px;width:736px;height:192px;border:1px solid var(--line);text-align:center;padding-top:30px}
.delivery h3{color:var(--purple);font-size:24px}
.delivery p{font-size:12px;color:var(--purple);width:420px;margin:10px auto 16px;line-height:1.5}

/* footer */
.footer{top:2160px;left:0;width:1200px;height:312px;background:var(--footer);color:#c9c6d6}
.col{top:40px;width:170px;font-size:11px;line-height:1.9}
.col h5{font-family:"Montserrat",Arial,sans-serif;color:var(--pink);font-size:13px;margin-bottom:8px}
.pay{display:flex;gap:6px;margin-top:8px}
.pay i{width:30px;height:18px;background:#d9d6e4;border-radius:2px}
.news input{width:170px;height:28px;border:none;background:#f2f1f7;padding:0 8px;font-size:11px}
.news .btn{width:170px;text-align:center;margin-top:8px;padding:8px 0}
.legal{top:2400px;left:232px;width:736px;border-top:1px solid #55506a;padding-top:14px;font-size:11px;color:#a7a3b8;display:flex;justify-content:space-between}
.social{display:flex;gap:10px}
.social i{width:24px;height:24px;border:1px solid #8d88a3;border-radius:2px}
</style>
</head>
<body>

<header>
  <div class="abs topbar">
    <div class="abs phone">1300 555 014</div>
    <div class="abs util"><span>Blog</span><span>Login / Register</span></div>
  </div>
  <div class="abs brand"><div class="dot"></div><span>Mirrowen Haven</span></div>
  <div class="abs search"><span>Search products…</span>
    <svg width="14" height="14" viewBox="0 0 14 14"><circle cx="6" cy="6" r="4.5" fill="none" stroke="#6a4fb8" stroke-width="1.6"/><line x1="9.5" y1="9.5" x2="13" y2="13" stroke="#6a4fb8" stroke-width="1.6"/></svg>
  </div>
  <div class="abs icons">
    <svg width="20" height="20" viewBox="0 0 20 20"><circle cx="10" cy="7" r="4" fill="none" stroke="#333344" stroke-width="1.5"/><path d="M3 18c1-4 4-5 7-5s6 1 7 5" fill="none" stroke="#333344" stroke-width="1.5"/></svg>
    <svg width="20" height="20" viewBox="0 0 20 20"><path d="M10 17 3 10a4 4 0 0 1 7-5 4 4 0 0 1 7 5z" fill="none" stroke="#333344" stroke-width="1.5"/></svg>
    <svg width="20" height="20" viewBox="0 0 20 20"><path d="M4 6h12l-1 11H5z" fill="none" stroke="#333344" stroke-width="1.5"/><path d="M7 6a3 3 0 0 1 6 0" fill="none" stroke="#333344" stroke-width="1.5"/></svg>
  </div>
  <nav class="abs nav">
    <span>Home</span><span>Health &amp; Body</span><span>Skincare</span><span>Hair &amp; Beauty</span><span>Home &amp; Baby</span><span>Natural Wellbeing</span><span>Eco Friendly Living</span><span>Aromatherapy</span>
  </nav>
</header>

<section class="abs hero" role="img" aria-label="Photo of a woman wearing a flower crown and bright vegan lipstick">
  <div class="abs copy">
    <h1>VEGAN LIPSTICK</h1>
    <p>Natural Certified Organic Colour</p>
    <span class="btn">Shop now</span>
  </div>
  <div class="abs arrow" style="left:14px;top:215px"><svg width="10" height="10" viewBox="0 0 10 10"><path d="M7 1 3 5l4 4" fill="none" stroke="#333" stroke-width="1.6"/></svg></div>
  <div class="abs arrow" style="right:14px;top:215px"><svg width="10" height="10" viewBox="0 0 10 10"><path d="M3 1l4 4-4 4" fill="none" stroke="#333" stroke-width="1.6"/></svg></div>
  <div class="abs dots"><i></i><i></i><i></i></div>
</section>

<h2 class="abs section-title" style="top:684px">FEATURED PRODUCTS</h2>

<div class="abs arrow" style="left:192px;top:860px;border:1px solid var(--line)"><svg width="10" height="10" viewBox="0 0 10 10"><path d="M7 1 3 5l4 4" fill="none" stroke="#888" stroke-width="1.6"/></svg></div>
<div class="abs arrow" style="left:982px;top:860px;border:1px solid var(--line)"><svg width="10" height="10" viewBox="0 0 10 10"><path d="M3 1l4 4-4 4" fill="none" stroke="#888" stroke-width="1.6"/></svg></div>

<div class="abs card" style="left:232px"><div class="shot"><div role="img" aria-label="Red lipstick product photo" style="background:linear-gradient(#c8262e,#2a2a2a)"></div></div><h4>Rosehip Lip Colour</h4><div class="sub">Verdalia Organic</div><div class="price">$29.95</div></div>
<div class="abs card" style="left:432px"><div class="shot"><div role="img" aria-label="Black jar of balm product photo" style="background:linear-gradient(#333,#111);border-radius:50%;height:90px"></div></div><h4>Jade Healing Balm</h4><div class="sub">Kindle Bloom</div><div class="price">$24.95</div></div>
<div class="abs card" style="left:632px"><div class="shot"><div role="img" aria-label="Mascara tube product photo" style="background:linear-gradient(#ddd,#777);width:20px"></div></div><h4>Mineral Volume Mascara</h4><div class="sub">Solenne Naturals</div><div class="price">$32.00</div></div>
<div class="abs card" style="left:832px"><div class="shot"><div role="img" aria-label="Jar of organic coconut oil product photo" style="background:linear-gradient(#e7eef2,#b9cfd8)"></div></div><h4>Organic Coconut Oil</h4><div class="sub">Orrin Pantry</div><div class="price">$18.50</div></div>

<section class="abs welcome">
  <div class="abs text">
    <small>Welcome to Mirrowen Haven</small>
    <h2>YOUR HEALTHY, NATURAL, TOXIN-FREE AND ORGANIC PRODUCTS SUPERSTORE.</h2>
    <p>Discover our range of natural and organic products for the whole family, chosen with care for you and the planet.</p>
    <span class="ghost">About us</span><span class="ghost">Shop now</span>
  </div>
  <div class="abs tile" style="left:608px;top:48px;width:224px;height:220px;background:linear-gradient(135deg,#c9743f,#7a8c45,#e0b25a)" role="img" aria-label="Photo of a colourful healthy salad"></div>
  <div class="abs tile" style="left:856px;top:48px;width:112px;height:100px;background:linear-gradient(135deg,#e88aa2,#b8d66c)" role="img" aria-label="Photo of fresh fruit and smoothie"></div>
  <div class="abs tile" style="left:856px;top:168px;width:112px;height:100px;background:linear-gradient(135deg,#6fbf6a,#d9e8a8)" role="img" aria-label="Photo of green juice"></div>
  <div class="abs tile" style="left:608px;top:288px;width:104px;height:112px;background:linear-gradient(135deg,#efe6da,#c9a67e)" role="img" aria-label="Photo of natural skincare products"></div>
  <div class="abs tile" style="left:728px;top:288px;width:104px;height:112px;background:linear-gradient(135deg,#e7a64a,#8fae62)" role="img" aria-label="Photo of fresh produce"></div>
  <div class="abs tile" style="left:856px;top:288px;width:112px;height:112px;background:linear-gradient(135deg,#c46d5e,#6e8e58)" role="img" aria-label="Photo of a healthy meal bowl"></div>
</section>

<h2 class="abs section-title" style="top:1616px">FEATURED BRANDS</h2>
<div class="abs brands">
  <svg width="10" height="14" viewBox="0 0 10 14"><path d="M8 1 2 7l6 6" fill="none" stroke="#999" stroke-width="1.6"/></svg>
  <span>Solenne</span><span>Verdalia</span><span>Kindle Bloom</span><span>Orrin</span><span>Pulse Leaf</span><span>Dewhaven</span>
  <svg width="10" height="14" viewBox="0 0 10 14"><path d="M2 1l6 6-6 6" fill="none" stroke="#999" stroke-width="1.6"/></svg>
</div>

<section class="abs delivery">
  <h3>FREE DELIVERY</h3>
  <p>On orders over $99 within Australia. Fast, carbon-neutral shipping to your door with recyclable packaging on every order.</p>
  <span class="btn">Shop now</span>
</section>

<footer class="abs footer">
  <div class="abs col" style="left:232px"><h5>Shop Online</h5>Home<br>Health &amp; Body<br>Skincare<br>Hair &amp; Beauty<br>Home &amp; Baby<br>Natural Wellbeing<br>Eco Friendly Living<br>Aromatherapy</div>
  <div class="abs col" style="left:420px"><h5>Customer Service</h5>My Account<br>Payments<br>Shipping<br>Returns<br>Privacy Policy<br>Terms &amp; Conditions<br>FAQs<br>Contact</div>
  <div class="abs col" style="left:608px"><h5>Contact Us</h5>Mirrowen Haven<br>12 Fernleigh Road<br>Byron Bay NSW 2481<br>Phone: 1300 555 014<br>hello@mirrowenhaven.com.au<br>
    <div style="width:30px;height:30px;border-radius:50%;background:#d9d6e4;margin-top:8px"></div>
    <div class="pay"><i></i><i></i><i></i><i></i></div>
  </div>
  <div class="abs col news" style="left:800px"><h5>Want the latest deals?</h5>Join our newsletter for offers and news.<br><input placeholder="Email address"><span class="btn">Subscribe</span></div>
</footer>
<div class="abs legal"><span>© Mirrowen Haven. All rights reserved. mirrowenhaven.com.au</span><div class="social"><i></i><i></i></div></div>

</body>
</html>
```